Sena & Kaan Wedding Invitation and Decorative Designs

We are looking for a sweet and elegant design for our wedding invitation. We need different versions of the same design to use both as printed hard copies and in digital formats (WhatsApp image, instagram post, etc) Please see attached sample invitation, which we like as a simple and elegant option, but also find it quite basic. We are open to creative suggestions following a similar style.
Once we decide on an invitation design, we would like to use the same design elements in guest name cards, welcome sign, menu cards and print cover for the dance floor of our wedding venue. Please see random samples of these materials attached. We also attach a photo from our wedding venue displaying a close to final visual of the decoration we chose for our wedding day (sharing in case it helps as an inspiration source and helps with matching decoration colors with the designs)
- Must have a style similar to the attached sample invitation

```html
<!DOCTYPE html>
<html lang="tr">
<head>
<meta charset="UTF-8">
<title>Sena & Kaan – Düğün Yemeği Daveti</title>
<link rel="stylesheet" href="https://fonts.googleapis.com/css2?family=Montserrat:wght@400;700&family=Pinyon+Script&display=swap">
<style>
  :root{
    --green-deep:#24502a;
    --green-ink:#1f4024;
    --green-line:#4f7f52;
    --time-grey:#3b3f3d;
    --paper:#ffffff;
    --wash:#a9cfc9;
    --leaf:#8fbf98;
  }
  html,body{margin:0;padding:0;overflow:hidden;background:var(--paper);}
  .invitation{
    position:relative;width:858px;height:1200px;overflow:hidden;
    background:var(--paper);font-family:"Montserrat",sans-serif;color:var(--green-ink);
  }
  .art{position:absolute;}
  .art--wash{
    left:-40px;top:380px;width:520px;height:840px;
    background:radial-gradient(ellipse at 10% 55%, rgba(120,175,168,.75) 0%, rgba(169,207,201,.45) 40%, rgba(255,255,255,0) 72%);
  }
  .art--leaves-top{
    left:-20px;top:80px;width:240px;height:420px;
    background:radial-gradient(ellipse at 35% 45%, rgba(143,191,152,.6) 0%, rgba(180,212,186,.3) 45%, rgba(255,255,255,0) 72%);
  }
  .art--blossom-right{
    right:-40px;top:520px;width:140px;height:280px;
    background:radial-gradient(ellipse at 80% 50%, rgba(210,214,212,.7) 0%, rgba(255,255,255,0) 70%);
  }
  .art--leaves-bottom{
    right:-30px;bottom:-30px;width:560px;height:420px;
    background:radial-gradient(ellipse at 75% 65%, rgba(120,170,130,.7) 0%, rgba(160,200,170,.4) 40%, rgba(255,255,255,0) 72%);
  }
  .art--daisy{
    left:340px;bottom:-30px;width:200px;height:140px;
    background:radial-gradient(ellipse at 50% 60%, #e2c045 0%, #e9cf6a 18%, #f6f6f2 32%, rgba(255,255,255,0) 70%);
  }
  .art--leaves-bottom-left{
    left:100px;bottom:-20px;width:260px;height:90px;
    background:radial-gradient(ellipse at 50% 70%, rgba(143,191,152,.55) 0%, rgba(255,255,255,0) 70%);
  }
  .content{position:absolute;inset:0;text-align:center;}
  .line{position:absolute;left:0;right:0;margin:0;}
  .welcome{top:64px;font-size:50px;font-weight:400;letter-spacing:2px;color:var(--green-ink);}
  .occasion{top:140px;font-size:22px;letter-spacing:1px;color:var(--green-ink);}
  .name{font-family:"Pinyon Script",cursive;color:var(--green-deep);font-weight:400;line-height:1;}
  .name--first{top:200px;font-size:104px;}
  .amp{top:344px;font-size:42px;color:var(--green-ink);}
  .name--second{top:386px;font-size:104px;}
  .message{top:528px;font-size:22px;line-height:29px;color:var(--green-ink);}
  .invited{top:604px;font-size:48px;font-weight:700;color:var(--green-deep);}
  .venue{top:686px;font-size:21px;line-height:29px;color:var(--green-ink);}
  .date{top:774px;font-size:27px;font-weight:700;color:var(--green-deep);}
  .schedule{position:absolute;top:864px;left:106px;width:660px;height:160px;display:flex;}
  .slot{flex:1;position:relative;display:flex;flex-direction:column;align-items:center;}
  .slot + .slot{border-left:2px solid var(--green-line);}
  .slot svg{margin-top:10px;width:66px;height:66px;}
  .slot__time{margin-top:38px;font-size:27px;color:var(--time-grey);}
  .rsvp{
    position:absolute;top:1054px;left:110px;width:460px;height:58px;
    background:linear-gradient(90deg, rgba(255,255,255,0) 0%, rgba(255,255,255,.85) 25%, rgba(255,255,255,.9) 80%, rgba(255,255,255,0) 100%);
  }
  .rsvp__text{top:1066px;font-size:28px;font-weight:700;color:var(--green-deep);}
</style>
</head>
<body>
<main class="invitation">
  <div class="art art--wash" role="img" aria-label="Soft sea-green watercolour wash"></div>
  <div class="art art--leaves-top" role="img" aria-label="Watercolour olive leaves branch"></div>
  <div class="art art--blossom-right" role="img" aria-label="Faded white flower at the edge"></div>
  <div class="art art--leaves-bottom" role="img" aria-label="Watercolour green leaves and white blossoms"></div>
  <div class="art art--leaves-bottom-left" role="img" aria-label="Watercolour leaves"></div>
  <div class="art art--daisy" role="img" aria-label="Watercolour daisy with yellow centre"></div>

  <section class="content">
    <h1 class="line welcome">HOŞ GELDİN</h1>
    <p class="line occasion">DÜĞÜN YEMEĞİNE</p>
    <p class="line name name--first">Sena</p>
    <p class="line amp">&amp;</p>
    <p class="line name name--second">Kaan</p>
    <p class="line message">Bu mutiu giint,imuzaie sizleri de arannzda gormekten<br>muttuluk duyacagiz.</p>
    <h2 class="line invited">Davetlisiniz</h2>
    <p class="line venue">KORUBAHÇE: Çamlık, Koru Sok. No: 14<br>Beykoz, Istanbul</p>
    <p class="line date">24 agustos 2024</p>

    <div class="schedule">
      <div class="slot">
        <svg viewBox="0 0 64 64" fill="none" stroke="#1f4024" stroke-width="3" stroke-linejoin="round">
          <path d="M4 20 L26 20 L15 36 Z" fill="#1f4024"/><path d="M15 36 V54 M9 56 H21"/>
          <path d="M34 14 L56 20 L41 34 Z" fill="#1f4024"/><path d="M41 34 L37 52 M31 54 L43 56"/>
          <path d="M20 10 L22 14 M28 8 L27 13 M44 6 L46 10"/>
        </svg>
        <span class="slot__time">18.00</span>
      </div>
      <div class="slot">
        <svg viewBox="0 0 64 64" fill="none" stroke="#1f4024" stroke-width="3">
          <circle cx="24" cy="36" r="16"/><circle cx="24" cy="36" r="11"/>
          <circle cx="40" cy="40" r="16"/><circle cx="40" cy="40" r="11"/>
          <path d="M17 12 a4 4 0 0 1 7 -3 a4 4 0 0 1 7 3 l-7 7 z"/>
        </svg>
        <span class="slot__time">19.00</span>
      </div>
      <div class="slot">
        <svg viewBox="0 0 64 64" fill="none" stroke="#1f4024" stroke-width="3">
          <circle cx="32" cy="34" r="24"/><circle cx="32" cy="34" r="16"/>
          <path d="M22 18 V32 M26 18 V32 M30 18 V32 M22 32 Q26 36 30 32 M26 34 V58"/>
          <path d="M40 58 V18 Q46 24 44 38 H40"/>
          <path d="M54 8 L55 12 L59 13 L55 14 L54 18 L53 14 L49 13 L53 12 Z"/>
        </svg>
        <span class="slot__time">20.00</span>
      </div>
      <div class="slot">
        <svg viewBox="0 0 64 64" fill="none" stroke="#1f4024" stroke-width="3" stroke-linejoin="round">
          <path d="M6 58 L22 24 L40 42 Z"/>
          <path d="M26 26 Q30 14 24 6 M36 34 Q46 26 58 30 M32 28 L48 12"/>
          <circle cx="40" cy="10" r="2.5"/><rect x="48" y="20" width="4" height="4"/>
          <circle cx="54" cy="44" r="3"/><path d="M10 8 L12 13 L17 13 L13 16 L15 21 L10 18 L5 21 L7 16 L3 13 L8 13 Z"/>
        </svg>
        <span class="slot__time">00.00</span>
      </div>
    </div>

    <div class="rsvp"></div>
    <p class="line rsvp__text">LCV: 02125550148</p>
  </section>
</main>
</body>
</html>
```